New Brochure for existing Virtual Reality Amusement Arena

I need a two sided half page brochure for my arcade. it needs to say what we do and what we have to offer. It basically needs to be a paper copy of all the information thats on my website www.kavimo-nix.com
Please check that as it is very informative!
Industry/Entity Type
Entertainment
Colors
Designer to choose colors to be used in the design.
Requirements
Must have
- Color. I have uploaded an old brochure I had made, but now we have a new company and new logo, please make it similar to that. Please pull all pics from my website www.kavimo-nix.com
Should not have
- useless information

```html
<!DOCTYPE html>
<html lang="en">
<head>
<meta charset="utf-8">
<title>Kavimo-Nix Virtual Reality Arena Brochure</title>
<link rel="stylesheet" href="https://fonts.googleapis.com/css2?family=Oswald:wght@400;600;700&family=Open+Sans:wght@400;600;700&display=swap">
<style>
:root{
  --navy:#16225a;
  --navy-deep:#0e1640;
  --blue:#2c56c9;
  --orange:#f7941d;
  --white:#ffffff;
  --ink:#1e2540;
  --muted:#5a6078;
  --page:#eceef3;
  --head:"Oswald",sans-serif;
  --body:"Open Sans",sans-serif;
}
*{margin:0;padding:0;box-sizing:border-box}
html,body{width:867px;height:1200px;overflow:hidden;background:var(--page);font-family:var(--body);color:var(--ink)}
.sheet{position:absolute;left:36px;width:795px;overflow:hidden;box-shadow:0 4px 14px rgba(0,0,0,.18)}
.sheet--outside{top:30px;height:535px;background:var(--navy)}
.sheet--inside{top:600px;height:560px;background:var(--white)}
.sheet svg.shapes{position:absolute;inset:0;width:100%;height:100%}
.abs{position:absolute}
.head{font-family:var(--head);text-transform:uppercase;line-height:1}
.brand{display:flex;align-items:center;gap:8px;font-family:var(--head);font-weight:700;letter-spacing:1px;color:var(--white);font-size:20px}
.brand__dot{width:22px;height:22px;border-radius:50%;background:var(--white)}
.brand--dark{color:var(--navy)}
.brand--dark .brand__dot{background:var(--navy)}
.small{font-size:8px;line-height:1.45}

/* outside */
.groups{left:18px;top:18px;width:230px;color:var(--white)}
.groups h2{font-size:20px;font-weight:600}
.groups h2 span{color:var(--orange)}
.groups p{margin-top:8px;color:#c9d0ea}
.cover-brand{left:305px;top:380px}
.contact{left:305px;top:420px;list-style:none;color:var(--white)}
.contact li{display:flex;align-items:center;gap:8px;font-size:8.5px;margin-bottom:7px}
.contact i{width:12px;height:12px;border-radius:50%;background:var(--orange);flex:none}
.cover-title{left:560px;top:205px;width:220px;text-align:right}
.cover-title .kicker{font-size:13px;color:var(--navy);font-weight:400}
.cover-title .main{font-size:22px;color:var(--navy);font-weight:700;margin-top:4px}
.cover-title .sub{font-size:8px;color:var(--muted);margin-top:6px;text-transform:none;font-family:var(--body)}

/* inside */
.gaming{left:16px;top:30px;width:220px;color:var(--white)}
.gaming .t1{font-size:34px;font-weight:700}
.gaming .t2{font-size:16px;color:var(--orange);font-weight:600;margin-top:2px}
.gaming p{margin-top:10px;width:170px;color:#e6ecf2}
.btn{display:inline-block;margin-top:12px;background:var(--orange);color:var(--white);font-family:var(--head);font-size:10px;padding:5px 12px;letter-spacing:1px}
.features{left:14px;top:230px;width:240px;display:grid;grid-template-columns:1fr 1fr;gap:26px 14px}
.feature__icon{width:30px;height:30px;background:var(--navy);display:flex;align-items:center;justify-content:center;margin-bottom:6px}
.feature h3{font-family:var(--head);font-size:13px;color:var(--navy);font-weight:600;margin-bottom:4px}
.feature:nth-child(even) h3{color:var(--orange)}
.feature p{color:var(--muted)}
.inside-brand{left:340px;top:18px}
.walk{left:285px;top:70px;width:225px;text-align:center}
.walk .w1{font-size:30px;color:var(--navy);font-weight:700}
.walk .w2{font-size:30px;color:var(--orange);font-weight:700}
.walk p{margin-top:8px;color:var(--muted)}
.schedule{left:282px;top:200px;width:232px;display:flex;gap:8px}
.schedule section{flex:1}
.schedule h4{font-family:var(--head);font-size:10px;font-weight:600;color:var(--white);padding:4px 6px;text-transform:uppercase}
.hours h4{background:var(--navy)}
.entries h4{background:var(--orange)}
.schedule ul{list-style:none;padding:6px;font-size:8px;line-height:1.7}
.hours ul{background:#e7eaf4}
.entries ul{background:#fdeedc}
.how{left:550px;top:22px;width:225px;text-align:right;color:var(--white)}
.how .h1{font-size:26px;font-weight:700}
.how .h1 span{color:var(--orange)}
.how p{margin-top:6px;color:#c9d0ea}
.how .fee{font-size:20px;font-weight:700;color:var(--orange);margin-top:12px}
.how .price{font-size:10px;font-family:var(--head);margin-top:4px}
.haptic{left:550px;top:450px;width:225px;text-align:right;color:var(--white)}
.haptic .h1{font-size:22px;font-weight:700;color:var(--orange)}
.haptic p{margin-top:6px;color:#c9d0ea}
</style>
</head>
<body>

<article class="sheet sheet--outside">
  <svg class="shapes" viewBox="0 0 795 535" preserveAspectRatio="none">
    <defs>
      <linearGradient id="gStations" x1="0" y1="0" x2="1" y2="1">
        <stop offset="0" stop-color="#4b5268"/><stop offset="1" stop-color="#1d2233"/>
      </linearGradient>
      <linearGradient id="gPlayerTop" x1="0" y1="0" x2="1" y2="1">
        <stop offset="0" stop-color="#3a66c8"/><stop offset="1" stop-color="#101a45"/>
      </linearGradient>
      <linearGradient id="gPlayerBottom" x1="0" y1="0" x2="1" y2="1">
        <stop offset="0" stop-color="#2b3f8f"/><stop offset=".6" stop-color="#15205a"/><stop offset="1" stop-color="#7a2f3a"/>
      </linearGradient>
    </defs>
    <rect width="795" height="535" fill="#16225a"/>
    <g role="img" aria-label="Photo of the arena's row of gaming stations with chairs">
      <rect x="0" y="140" width="265" height="395" fill="url(#gStations)"/>
    </g>
    <polygon points="110,140 360,300 110,460" fill="#ffffff"/>
    <polygon points="265,140 400,300 265,460" fill="none" stroke="#2c56c9" stroke-width="3"/>
    <polygon points="265,0 530,0 530,140 420,0" fill="#0e1640"/>
    <g role="img" aria-label="Photo of a player wearing a VR headset">
      <polygon points="530,0 795,0 795,150 530,190" fill="url(#gPlayerTop)"/>
    </g>
    <polygon points="530,190 795,150 795,300 530,300" fill="#ffffff"/>
    <g role="img" aria-label="Photo of a player in action in the VR arena">
      <rect x="530" y="300" width="265" height="235" fill="url(#gPlayerBottom)"/>
    </g>
    <polygon points="530,300 610,420 530,535" fill="#f7941d"/>
    <polygon points="470,300 530,300 530,535 470,535" fill="#16225a"/>
  </svg>

  <div class="abs groups">
    <h2 class="head">Groups<span>/</span>Parties</h2>
    <p class="small">Host birthdays, team outings and celebrations in our private arena. Groups of eight or more enjoy reserved bays, party packages and a dedicated host.</p>
  </div>

  <div class="abs brand cover-brand"><span class="brand__dot"></span>KAVIMO-NIX</div>
  <ul class="abs contact">
    <li><i></i>1200 Orbit Lane, Suite 4, Riverton</li>
    <li><i></i>www.kavimo-nix.com</li>
    <li><i></i>play@kavimo-nix.com</li>
    <li><i></i>(555) 014-2290</li>
    <li><i></i>@kavimonix</li>
  </ul>

  <div class="abs cover-title">
    <div class="head kicker">A Virtual Reality</div>
    <div class="head main">Gaming like you've never seen</div>
    <div class="head sub">Step inside worlds built for you</div>
  </div>
</article>

<article class="sheet sheet--inside">
  <svg class="shapes" viewBox="0 0 795 560" preserveAspectRatio="none">
    <defs>
      <linearGradient id="gArena" x1="0" y1="0" x2="1" y2="1">
        <stop offset="0" stop-color="#2f6b3c"/><stop offset="1" stop-color="#0f2a1c"/>
      </linearGradient>
      <linearGradient id="gFloor" x1="0" y1="0" x2="1" y2="1">
        <stop offset="0" stop-color="#3457b8"/><stop offset="1" stop-color="#0e1640"/>
      </linearGradient>
      <linearGradient id="gHaptic" x1="0" y1="0" x2="0" y2="1">
        <stop offset="0" stop-color="#4a6fd6"/><stop offset="1" stop-color="#16225a"/>
      </linearGradient>
    </defs>
    <g role="img" aria-label="Photo of players in the green-lit VR arena">
      <polygon points="0,0 265,0 265,180 0,210" fill="url(#gArena)"/>
    </g>
    <polygon points="0,210 265,180 265,188 0,218" fill="#f7941d"/>
    <g role="img" aria-label="Photos of guests playing in the arena">
      <polygon points="265,430 530,400 530,560 265,560" fill="url(#gFloor)"/>
    </g>
    <rect x="530" y="0" width="265" height="560" fill="#16225a"/>
    <g role="img" aria-label="Photo of a player feeling haptic feedback through a vest">
      <polygon points="530,170 795,200 795,430 530,400" fill="url(#gHaptic)"/>
    </g>
    <polygon points="530,170 600,185 530,250" fill="#f7941d"/>
  </svg>

  <div class="abs gaming">
    <div class="head t1">Gaming</div>
    <div class="head t2">Like you've never seen</div>
    <p class="small">Premium virtual reality for every age and skill level.</p>
    <span class="btn">BOOK NOW</span>
  </div>

  <div class="abs features">
    <div class="feature">
      <div class="feature__icon"><svg width="16" height="16" viewBox="0 0 16 16"><circle cx="8" cy="8" r="6" fill="none" stroke="#fff" stroke-width="2"/></svg></div>
      <h3>Immersive</h3>
      <p class="small">Full 360 degree worlds that surround you with sight and sound.</p>
    </div>
    <div class="feature">
      <div class="feature__icon"><svg width="18" height="12" viewBox="0 0 18 12"><rect x="1" y="1" width="16" height="10" rx="3" fill="none" stroke="#fff" stroke-width="2"/></svg></div>
      <h3>Orbix</h3>
      <p class="small">Premium headsets with precise tracking for crisp, smooth gameplay.</p>
    </div>
    <div class="feature">
      <div class="feature__icon"><svg width="16" height="16" viewBox="0 0 16 16"><path d="M4 2v8h8v4" fill="none" stroke="#fff" stroke-width="2"/></svg></div>
      <h3>Seated</h3>
      <p class="small">Relaxed experiences for racing, flying and cinematic adventures.</p>
    </div>
    <div class="feature">
      <div class="feature__icon"><svg width="16" height="16" viewBox="0 0 16 16"><path d="M2 8h11M9 4l4 4-4 4" fill="none" stroke="#fff" stroke-width="2"/></svg></div>
      <h3>Free Roam</h3>
      <p class="small">Walk freely through large arenas with friends as a squad.</p>
    </div>
  </div>

  <div class="abs brand brand--dark inside-brand"><span class="brand__dot"></span>KAVIMO-NIX</div>
  <div class="abs walk">
    <div class="head w1">Just Walk</div>
    <div class="head w2">Right In</div>
    <p class="small">No booking needed. Drop in any time during opening hours and play.</p>
  </div>

  <div class="abs schedule">
    <section class="hours">
      <h4>Hours of Operation</h4>
      <ul>
        <li>Monday Closed</li>
        <li>Tuesday 12PM - 9PM</li>
        <li>Wednesday 12PM - 9PM</li>
        <li>Thursday 12PM - 9PM</li>
        <li>Friday 12PM - 11PM</li>
        <li>Saturday 10AM - 11PM</li>
        <li>Sunday 10AM - 8PM</li>
      </ul>
    </section>
    <section class="entries">
      <h4>Entry Times</h4>
      <ul>
        <li>Weekdays: 12PM, 2PM, 4PM</li>
        <li>Evenings: 6PM, 8PM</li>
        <li>Weekends: 10AM, 12PM, 2PM</li>
        <li>Late: 4PM, 6PM, 8PM</li>
      </ul>
    </section>
  </div>

  <div class="abs how">
    <div class="head h1">How <span>it works</span></div>
    <p class="small">Choose a game, gear up and play.</p>
    <div class="head fee">Entry Fee</div>
    <div class="head price">$25 per person / 30 minutes</div>
  </div>

  <div class="abs haptic">
    <div class="head h1">Haptic Feedback</div>
    <p class="small">Feel every impact through vests that bring the action to life.</p>
  </div>
</article>

</body>
</html>
```